Q9 Clinic business card design

It is a doctor's business card. It will include both English and Chinese information ( will be provided). The design should look professional. It is an obstetrics and gynaecology clinic.

Target Market(s)

Hong Kong private medical market_adult females

Contact Information for Business Card

as the information provided_color coordination with the logo color

Font styles to use
Sans Serif

Colors

Designer to choose colors to be used in the design.

Requirements
Must have
• Logo.
• dr's name, credentials, address, telephone, fax no,

```html
<!DOCTYPE html>
<html lang="en">
<head>
<meta charset="utf-8">
<title>Q9 Clinic business card</title>
<link href="https://fonts.googleapis.com/css2?family=Open+Sans:wght@400;600;700&family=Noto+Sans+TC:wght@400;500;700&display=swap" rel="stylesheet">
<style>
:root{
  --bg:#e4e6e8;
  --card:#ffffff;
  --blue:#1a7fc4;
  --blue-deep:#1c5fa8;
  --sky:#1ea2dc;
  --green:#79b531;
  --grey:#8a8f94;
  --ink:#2b2f33;
  --on-dark:#f3f8ec;
}
*{margin:0;padding:0;box-sizing:border-box}
html,body{width:1200px;height:997px;overflow:hidden;background:var(--bg)}
body{font-family:"Open Sans",Arial,sans-serif;color:var(--ink)}
.sheet{position:relative;width:1200px;height:997px}
.card{position:absolute;left:220px;width:760px;height:434px;background:var(--card);border-radius:22px;overflow:hidden;box-shadow:0 6px 18px rgba(0,0,0,.18)}
.card--back{top:40px}
.card--front{top:523px}
.bands{position:absolute;left:0;top:0;width:760px;height:434px}
.brand{position:absolute;left:0;right:0;top:66px;text-align:center}
.brand__name{font-family:"Open Sans",sans-serif;font-weight:700;font-size:46px;line-height:1;color:var(--blue-deep)}
.brand__tag{margin-top:10px;font-weight:600;font-size:14px;letter-spacing:3px;color:var(--grey)}
.doctor{position:absolute;left:0;right:0;top:172px;text-align:center}
.doctor__name{font-weight:700;font-size:19px;color:var(--blue-deep);letter-spacing:.5px}
.doctor__creds{font-size:13.5px;color:var(--ink);margin-top:1px}
.doctor--zh{top:150px}
.doctor--zh .doctor__name{font-family:"Noto Sans TC",sans-serif;font-size:17px}
.doctor--zh .doctor__creds{font-family:"Noto Sans TC",sans-serif;font-size:12.5px;line-height:1.45;color:#3c4146}
.contacts{position:absolute;left:0;right:0;display:flex;justify-content:center;gap:26px;font-size:15px;font-weight:600;color:var(--blue)}
.card--front .contacts{top:236px}
.card--back .contacts{top:252px}
.contact{display:flex;align-items:center;gap:7px}
.contact svg{width:18px;height:18px}
.section-title{position:absolute;left:0;right:0;top:288px;text-align:center;font-size:13px;letter-spacing:1.5px;color:#fff;font-weight:600}
.card--back .section-title{font-family:"Noto Sans TC",sans-serif;letter-spacing:3px}
.addresses{position:absolute;left:40px;right:40px;top:326px;display:flex;justify-content:space-between;color:var(--on-dark);font-size:14px;line-height:1.45}
.addresses address{font-style:normal;width:320px}
.addresses address:last-child{text-align:right}
.card--back .addresses{font-family:"Noto Sans TC",sans-serif;top:340px}
</style>
</head>
<body>
<main class="sheet">

  <section class="card card--back" lang="zh-Hant">
    <svg class="bands" viewBox="0 0 760 434" aria-hidden="true">
      <path d="M0 282 L760 272 L760 434 L0 434 Z" fill="var(--sky)"/>
      <path d="M0 318 L760 306 L760 434 L0 434 Z" fill="var(--green)"/>
    </svg>
    <div class="brand" style="top:58px">
      <div class="brand__name" lang="en">Q9 Clinic</div>
      <div class="brand__tag" lang="en">OBSTETRICS . GYNAECOLOGY</div>
    </div>
    <div class="doctor doctor--zh">
      <div class="doctor__name">林偉明醫生</div>
      <div class="doctor__creds">香港中文大學內外全科醫學士　香港中文大學醫學博士<br>香港醫學專科學院院士(婦產科)　香港婦產科學院院士<br>英國皇家婦產科醫學院院士</div>
    </div>
    <div class="contacts">
      <span class="contact"><svg viewBox="0 0 18 18"><circle cx="9" cy="9" r="9" fill="var(--blue)"/><path d="M5.5 5.2c.6-.6 1.3-.5 1.6.1l.8 1.4c.2.4 0 .8-.3 1l-.5.4c.5 1 1.3 1.8 2.3 2.3l.4-.5c.3-.3.7-.4 1-.3l1.4.8c.6.3.7 1 .1 1.6-.9.9-2.2 1-3.5.1-1.5-1-2.6-2.1-3.6-3.6-.8-1.3-.7-2.6.2-3.5z" fill="#fff"/></svg>0161 555 0142</span>
      <span class="contact"><svg viewBox="0 0 18 18"><circle cx="9" cy="9" r="9" fill="var(--blue)"/><rect x="6.2" y="4" width="5.6" height="10" rx="1" fill="#fff"/><rect x="7" y="5.2" width="4" height="6.6" fill="var(--blue)"/></svg>07700 900 214</span>
      <span class="contact"><svg viewBox="0 0 18 18"><circle cx="9" cy="9" r="9" fill="var(--blue)"/><rect x="4.5" y="6" width="9" height="6.5" rx=".8" fill="#fff"/><path d="M4.8 6.4 9 9.6l4.2-3.2" stroke="var(--blue)" stroke-width="1" fill="none"/></svg>07700 900 388</span>
    </div>
    <div class="section-title">診所地址</div>
    <div class="addresses">
      <address>沙田柳樹街5號蓮苑8樓802室</address>
      <address>尖沙咀海港道88號雪松廣場B座6樓610室</address>
    </div>
  </section>

  <section class="card card--front">
    <svg class="bands" viewBox="0 0 760 434" aria-hidden="true">
      <path d="M0 282 L760 272 L760 434 L0 434 Z" fill="var(--sky)"/>
      <path d="M0 318 L760 306 L760 434 L0 434 Z" fill="var(--green)"/>
    </svg>
    <div class="brand">
      <div class="brand__name">Q9 Clinic</div>
      <div class="brand__tag">OBSTETRICS . GYNAECOLOGY</div>
    </div>
    <div class="doctor">
      <div class="doctor__name">DR LAM WAI MING, HENRY</div>
      <div class="doctor__creds">MBChB, MD, FHKAM(O&amp;G), FHKCOG, FRCOG</div>
    </div>
    <div class="contacts">
      <span class="contact"><svg viewBox="0 0 18 18"><circle cx="9" cy="9" r="9" fill="var(--blue)"/><path d="M5.5 5.2c.6-.6 1.3-.5 1.6.1l.8 1.4c.2.4 0 .8-.3 1l-.5.4c.5 1 1.3 1.8 2.3 2.3l.4-.5c.3-.3.7-.4 1-.3l1.4.8c.6.3.7 1 .1 1.6-.9.9-2.2 1-3.5.1-1.5-1-2.6-2.1-3.6-3.6-.8-1.3-.7-2.6.2-3.5z" fill="#fff"/></svg>0161 555 0142</span>
      <span class="contact"><svg viewBox="0 0 18 18"><circle cx="9" cy="9" r="9" fill="var(--blue)"/><rect x="6.2" y="4" width="5.6" height="10" rx="1" fill="#fff"/><rect x="7" y="5.2" width="4" height="6.6" fill="var(--blue)"/></svg>07700 900 214</span>
      <span class="contact"><svg viewBox="0 0 18 18"><circle cx="9" cy="9" r="9" fill="var(--blue)"/><rect x="4.5" y="6" width="9" height="6.5" rx=".8" fill="#fff"/><path d="M4.8 6.4 9 9.6l4.2-3.2" stroke="var(--blue)" stroke-width="1" fill="none"/></svg>07700 900 388</span>
    </div>
    <div class="section-title">OUR CLINIC ADDRESSES</div>
    <div class="addresses">
      <address>Unit 802, 8th floor, Lotus Court,<br>5 Willow Street, Shatin,<br>New Territories, HONG KONG</address>
      <address>Unit 610, 6th floor, Tower B, Cedar Place,<br>88 Harbour Road, Tsimshatsui,<br>Kowloon, HONG KONG</address>
    </div>
  </section>

</main>
</body>
</html>
```